Clever Cargo Trike Ad Campaign

I've started a cargo trike company in Washington, DC that will generate revenue from deliveries, promotions and advertising. The trikes have three large ad panel spaces that are perfect for banners. While I'll be using these for promoting customer products/services, I'd like a creative ad that also promotes my own company when not promoting others.

The trikes are human pedal powered, with electric-assist. They can carry 550 lbs and 62 cubic feet of cargo anywhere in DC's downtown area. They make no noise, don't block streets while delivering goods, move around town as quickly as vans or trucks, have zero tailipipe emissions, can use bike lanes, reduce street congestion, etc. In shortly, they are eco-friendly, low-impact, socially-responsible, dependable and efficient!

I'd also like to convey that the trikes are available for advertising and promotional campaigns.....

I'd like a campaign that conveys some of the above, but in a clever, (maybe even humorous) fashion. Not sure if each of three panels (54"x30", 54"x30", 37"x33") needs same ad or just similar ones. Campaign should be geared toward potential customers (organic drycleaners, bakeries, office supply, caterers, farmshare food deliveries, etc), but also be pertinent to anyone who views.

I've included our company logo and a graphic I created that shows the DC skyline (as yet unused). Also included a photo of one of the trikes.

Target Market(s)

* Businesses within Washington, DC that are seeking a unique delivery service.
* Large/small businesses seeking a dedicated, effective ad campaign venue in DC
* Any business seeking to promote products/services (hand out samples or brochures, represent them a street fairs, etc.)

Industry/Entity Type

It Company

Requirements
Must have
• I can easily come up with my own plain, straightforward ad campaign. I'm looking for something creative, unique, attractive that doesn't overwhelm the customer with information. I want it to convey what we have to offer potential customers.
Nice to have
• It would be great it if were humorous, had some kind of Washington focus, etc. But these are not crucial. While I'd like to somehow address the "eco-friendly" aspect of the company, I don't want this to be the sole focus.
• Thus, we can use colors other than the green in my logo, as long as they go well with what I have.
Should not have
• While I'm no fan of today's DC political environment, I don't want a campaign that will bring adverse attention to my company.

```html
<!DOCTYPE html>
<html lang="en">
<head>
<meta charset="utf-8">
<title>Cargo Trike Panels</title>
<link rel="stylesheet" href="https://fonts.googleapis.com/css2?family=Open+Sans:wght@400;500;600;700&family=Roboto:wght@500;700&display=swap">
<style>
  :root{
    --brand-green:#0f8c37;
    --ink:#0b0b0b;
    --paper:#ffffff;
    --backdrop-center:#ffffff;
    --backdrop-edge:#d9d9d9;
  }
  *{margin:0;padding:0;box-sizing:border-box}
  html,body{width:1200px;height:1200px;overflow:hidden}
  body{
    position:relative;
    background:radial-gradient(ellipse at 50% 50%, var(--backdrop-center) 0%, #f1f1f1 45%, var(--backdrop-edge) 100%);
    font-family:"Open Sans", Arial, sans-serif;
    color:var(--ink);
  }
  .size-label{
    position:absolute;
    font-family:Arial, Helvetica, sans-serif;
    font-weight:700;
    font-size:35px;
    letter-spacing:-0.5px;
    line-height:1;
  }
  .panel{position:absolute;background:var(--paper);overflow:hidden}
  .panel-wide{left:255px;width:690px;height:361px}
  .panel-wide .green-field{position:absolute;left:0;top:0;width:100%;height:269px;background:var(--brand-green)}
  .headline{
    position:absolute;left:0;width:100%;text-align:center;
    color:var(--paper);font-weight:500;white-space:nowrap;line-height:1;
  }
  .headline .dark{color:var(--ink)}
  .benefit-row{position:absolute;left:0;width:100%;top:0;height:100%}
  .benefit{position:absolute;width:130px;margin-left:-65px;text-align:center}
  .benefit svg{display:block;margin:0 auto;width:76px;height:76px}
  .benefit-label{
    display:block;margin-top:5px;color:var(--paper);
    font-size:12px;font-weight:700;letter-spacing:-0.2px;white-space:nowrap;
  }
  .brand-name{
    position:absolute;left:0;width:100%;text-align:center;
    font-family:"Open Sans", Arial, sans-serif;font-weight:700;
    color:var(--brand-green);letter-spacing:1px;line-height:1;
  }
  .panel-square{left:396px;top:806px;width:418px;height:394px}
  .panel-square .headline-green{
    position:absolute;left:0;width:100%;top:40px;text-align:center;
    font-family:Roboto, Arial, sans-serif;font-weight:500;
    color:var(--brand-green);font-size:27px;line-height:35px;letter-spacing:-0.3px;
  }
  .panel-square .url-band{
    position:absolute;left:0;bottom:0;width:100%;height:130px;background:var(--brand-green);
    display:flex;align-items:center;justify-content:center;
    color:var(--paper);font-size:33px;font-weight:400;
  }
</style>
</head>
<body>

<svg width="0" height="0" style="position:absolute">
  <defs>
    <symbol id="icon-no-noise" viewBox="0 0 80 80">
      <circle cx="40" cy="40" r="37" fill="#fff"/>
      <circle cx="40" cy="40" r="31" fill="none" stroke="#0f8c37" stroke-width="5"/>
      <path d="M20 33h8l12-10v34l-12-10h-8z" fill="#0b0b0b"/>
      <path d="M45 30a12 12 0 0 1 0 20M50 25a19 19 0 0 1 0 30M55 21a25 25 0 0 1 0 38" fill="none" stroke="#0b0b0b" stroke-width="3"/>
      <line x1="18" y1="62" x2="62" y2="18" stroke="#0f8c37" stroke-width="7"/>
    </symbol>
    <symbol id="icon-no-traffic" viewBox="0 0 80 80">
      <circle cx="40" cy="40" r="37" fill="#fff"/>
      <circle cx="40" cy="40" r="31" fill="none" stroke="#0f8c37" stroke-width="5"/>
      <path d="M16 50v-8l4-8h12l4 8v8z" fill="#0b0b0b"/>
      <path d="M44 50v-8l4-8h12l4 8v8z" fill="#0b0b0b"/>
      <line x1="18" y1="62" x2="62" y2="18" stroke="#0f8c37" stroke-width="7"/>
    </symbol>
    <symbol id="icon-fast" viewBox="0 0 80 80">
      <circle cx="40" cy="40" r="34" fill="none" stroke="#fff" stroke-width="6" stroke-dasharray="3 3"/>
      <circle cx="40" cy="40" r="28" fill="none" stroke="#fff" stroke-width="2"/>
      <text x="41" y="37" text-anchor="middle" font-family="Arial, sans-serif" font-size="10" fill="#fff">FAST</text>
      <text x="40" y="49" text-anchor="middle" font-family="Arial, sans-serif" font-size="10" fill="#fff">DELIVERY</text>
    </symbol>
    <symbol id="icon-eco" viewBox="0 0 80 80">
      <path id="eco-ring" d="M40 12a28 28 0 1 1 -0.1 0" fill="none"/>
      <text font-family="Arial, sans-serif" font-size="9" font-weight="700" fill="#fff" letter-spacing="0.5">
        <textPath href="#eco-ring">ECO FRIENDLY · ECO FRIENDLY ·</textPath>
      </text>
      <circle cx="40" cy="40" r="15" fill="none" stroke="#fff" stroke-width="3"/>
      <circle cx="35" cy="35" r="4" fill="#fff"/>
      <circle cx="45" cy="35" r="4" fill="#fff"/>
      <circle cx="35" cy="45" r="4" fill="#fff"/>
      <circle cx="45" cy="45" r="4" fill="#fff"/>
    </symbol>
  </defs>
</svg>

<div class="size-label" style="left:93px;top:153px">54”x30”</div>
<div class="size-label" style="left:93px;top:571px">54”x30”</div>
<div class="size-label" style="left:214px;top:975px">37”x33”</div>

<section class="panel panel-wide" style="top:27px">
  <div class="green-field"></div>
  <div class="headline" style="top:58px;font-size:45px">THE BEST <span class="dark">CARGO TRIKE IN</span></div>
  <div class="headline" style="top:116px;font-size:45px">WASHINGTON DC</div>
  <div class="benefit-row">
    <div class="benefit" style="left:143px;top:167px"><svg><use href="#icon-no-noise"/></svg><span class="benefit-label">NO NOISE</span></div>
    <div class="benefit" style="left:271px;top:167px"><svg><use href="#icon-no-traffic"/></svg><span class="benefit-label">NO TRAFFIC JAM</span></div>
    <div class="benefit" style="left:407px;top:167px"><svg><use href="#icon-fast"/></svg><span class="benefit-label">FAST DELIVERY</span></div>
    <div class="benefit" style="left:539px;top:167px"><svg><use href="#icon-eco"/></svg><span class="benefit-label">ECO FRIENDLY</span></div>
  </div>
  <div class="brand-name" style="top:295px;font-size:40px">HAULWISE</div>
</section>

<section class="panel panel-wide" style="top:417px">
  <div class="green-field"></div>
  <div class="headline" style="top:34px;font-size:32px">STUCK IN TRAFFIC ?&nbsp; <span class="dark">NOT ANYMORE</span></div>
  <div class="headline" style="top:79px;font-size:42px">CHOOSE US</div>
  <div class="benefit-row">
    <div class="benefit" style="left:143px;top:167px"><svg><use href="#icon-no-noise"/></svg><span class="benefit-label">NO NOISE</span></div>
    <div class="benefit" style="left:271px;top:167px"><svg><use href="#icon-no-traffic"/></svg><span class="benefit-label">NO TRAFFIC JAM</span></div>
    <div class="benefit" style="left:407px;top:167px"><svg><use href="#icon-fast"/></svg><span class="benefit-label">FAST DELIVERY</span></div>
    <div class="benefit" style="left:539px;top:167px"><svg><use href="#icon-eco"/></svg><span class="benefit-label">ECO FRIENDLY</span></div>
  </div>
  <div class="brand-name" style="top:295px;font-size:40px">HAULWISE</div>
</section>

<section class="panel panel-square">
  <div class="headline-green">THE BEST CARGO DELIVERY<br>SERVICE</div>
  <div class="brand-name" style="top:191px;font-size:36px">HAULWISE</div>
  <div class="url-band">haulwise-go.com</div>
</section>

</body>
</html>
```